Engineering and Energy service provider

We need a design that gives the impression of a high level of technical competence and a reliable partner. Simple structure with little need for updates.
The company brand is Valomir and today consists of two main businesses: energy optimisation (Valomir energy) and technical consultancy (Valomir Engineering). Valomir energy is shown in the attached powerpoint,
We are a young growing company that consists of several businesses, the largest parts are energy monitoring services and consulting services. Consulting services for commercial installations in the technical area of cooling, ventilation, heating and energy. Services offered include project planning, project management, inspection, operational analysis and technical investigations. Energy monitoring and optimization services are performed as a subscription with a subscription to the service.
Updates
Bug in system deadline before launch
Target Market(s)
Commercial property owners Grocery retail, grocery stores, construction companies
Industry/Entity Type
energy services and consulting services
Coding
Coded - Design and coding required
Number of Pages Required
5+ page
Look and feel
Each slider illustrates characteristics of the customer's brand and the style your logo design should communicate.

```html
<!DOCTYPE html>
<html lang="en">
<head>
<meta charset="utf-8">
<title>Valomir – Smart Energy, Reliable Results</title>
<link href="https://fonts.googleapis.com/css2?family=Krona+One&family=Poppins:wght@400;500;600&display=swap" rel="stylesheet">
<style>
:root{
  --blue:#0a4ea6;
  --blue-dark:#083f88;
  --orange:#f07a1c;
  --orange-2:#f5a21a;
  --ink:#1d1d1f;
  --muted:#555;
  --grey:#f3f3f3;
  --white:#fff;
}
*{box-sizing:border-box;margin:0;padding:0}
html,body{width:1200px;height:4208px;overflow:hidden}
body{font-family:"Poppins",sans-serif;color:var(--ink);position:relative;background:var(--white)}
.abs{position:absolute}
.display{font-family:"Krona One",sans-serif;text-transform:uppercase;letter-spacing:0;line-height:1.18}
.btn{position:absolute;display:flex;align-items:center;justify-content:center;background:linear-gradient(90deg,var(--orange),var(--orange-2));color:#fff;font-size:10px;font-weight:600;text-transform:uppercase;letter-spacing:.3px}
.photo{position:absolute}
.topbar{left:526px;top:0;width:674px;height:26px;background:var(--blue);clip-path:polygon(14px 0,100% 0,100% 100%,0 100%);color:#fff;font-size:10px;display:flex;align-items:center;padding-left:30px;gap:24px}
.topbar .social{margin-left:auto;display:flex;gap:16px;padding-right:20px}
.dot{width:6px;height:6px;border-radius:50%;background:#fff;display:inline-block}
.logo{font-family:"Poppins",sans-serif;font-weight:600;color:var(--blue);font-size:34px;letter-spacing:3px}
.nav{left:524px;top:46px;display:flex;gap:24px;font-size:10px;color:#333;text-transform:uppercase;align-items:center}
.hero-bg{left:0;top:98px;width:1200px;height:625px;background:linear-gradient(100deg,#6c6c6c 0%,#8a8f96 45%,#6b6f73 75%,#8d7a5e 100%)}
.slides{left:112px;top:548px;display:flex;gap:24px;color:#fff;font-size:10px}
.slides span{width:36px;border-top:1px solid #fff;padding-top:8px}
.scroll{left:40px;top:318px;color:#fff;font-size:8px;writing-mode:vertical-rl;letter-spacing:1px}
.side-social{left:1136px;top:268px;display:flex;flex-direction:column;gap:18px;align-items:center;color:#fff;font-size:8px}
.grey-band{left:0;top:1282px;width:1200px;height:630px;background:var(--grey)}
.about h2{left:599px;top:903px;font-size:29px;color:#222}
.about h3{left:599px;top:1058px;font-size:15px}
.about p{left:599px;top:1091px;width:455px;font-size:12px;line-height:1.55;color:var(--muted)}
.section-title{left:0;width:1200px;text-align:center}
.card{position:absolute;top:1551px;width:234px;height:268px;background:#fff}
.card .img{height:147px}
.card h4{font-family:"Krona One",sans-serif;font-size:12px;text-transform:uppercase;padding:18px 15px 0;line-height:1.45;color:#222}
.card p{font-size:11px;color:var(--muted);padding:10px 15px 0;line-height:1.6}
.opt h2{left:335px;width:530px;text-align:center;top:2055px;font-size:25px;color:#222}
.opt p{left:350px;width:500px;top:2150px;text-align:center;font-size:11px;line-height:1.6;color:var(--muted)}
.sectors{left:0;top:2436px;width:1200px;height:444px;background:var(--blue)}
.sector{position:absolute;top:2521px;height:275px;background:#fff}
.sector .img{height:176px}
.sector h4{font-family:"Krona One",sans-serif;font-size:11px;text-transform:uppercase;text-align:center;margin-top:26px;line-height:1.5;color:#222}
.arrow{position:absolute;top:2703px;width:36px;height:36px;display:flex;align-items:center;justify-content:center}
.contact h2{left:671px;top:3031px;font-size:30px;color:#222}
.field label{position:absolute;font-size:8px;font-weight:600;text-transform:uppercase}
.input{position:absolute;left:673px;width:297px;height:36px;background:var(--grey);font-size:9px;color:#888;padding:12px 20px}
.footer{left:0;top:3727px;width:1200px;height:481px;background:var(--blue)}
.banner{left:113px;top:3633px;width:973px;height:160px;background:linear-gradient(90deg,var(--orange) 0%,#f49a1d 60%,#f4c11e 100%)}
.foot-h{font-family:"Krona One",sans-serif;color:#fff;font-size:12px;text-transform:uppercase;top:3908px}
.foot-list{top:3944px;color:#fff;font-size:10px;line-height:26px;list-style:none}
</style>
</head>
<body>

<header>
  <div class="abs topbar">
    <span>&#9990; (+100)555-0142</span>
    <span>&#9993; hello@valomir-mail.com</span>
    <span class="social"><i class="dot"></i><i class="dot"></i><i class="dot"></i><i class="dot"></i></span>
  </div>
  <div class="abs logo" style="left:114px;top:40px">VALOMIR</div>
  <nav class="abs nav">
    <svg width="12" height="12" viewBox="0 0 12 12"><path d="M6 1 L11 6 H9.5 V11 H2.5 V6 H1 Z" fill="#f07a1c"/></svg>
    <span>About us</span><span>Services</span><span>Industries</span><span>Latest news</span><span>Careers</span>
    <span class="btn" style="position:static;width:110px;height:36px">Contact us</span>
  </nav>
</header>

<section>
  <div class="abs hero-bg" role="img" aria-label="Technician kneeling by solar panels with a drill and measuring equipment"></div>
  <div class="abs scroll">SCROLL DOWN</div>
  <h1 class="abs display" style="left:110px;top:320px;color:#fff;font-size:35px">Smart energy.<br>Reliable results.</h1>
  <p class="abs" style="left:112px;top:416px;color:#fff;font-size:12px;line-height:1.6;width:480px">Empowering commercial buildings with intelligent monitoring, optimization, and consulting solutions.</p>
  <a class="btn" style="left:110px;top:469px;width:152px;height:34px">Get a consultation</a>
  <div class="abs slides"><span>01</span><span>02</span><span>03</span><span>04</span></div>
  <div class="abs side-social"><span style="writing-mode:vertical-rl">VIDEOS</span><i class="dot"></i><i class="dot"></i><span style="width:22px;height:22px;border-radius:50%;background:var(--blue);display:block"></span><i class="dot"></i><i class="dot"></i></div>
</section>

<section class="about">
  <div class="abs grey-band"></div>
  <div class="photo" style="left:114px;top:836px;width:405px;height:544px;background:linear-gradient(135deg,#1f3c6e,#3f6fb0 45%,#9dbb3a 80%,#55606c)" role="img" aria-label="Engineer in a hard hat monitoring an energy control dashboard"></div>
  <h2 class="abs display">Your partner in<br>energy efficiency &amp;<br>technical excellence</h2>
  <h3 class="abs display">Valomir energy</h3>
  <p class="abs">We are a young and growing company with a strong technical background in energy monitoring and consulting. Our team specializes in cooling, ventilation, heating, and energy systems — delivering data-driven insights and reliable solutions for commercial installations.</p>
  <a class="btn" style="left:599px;top:1184px;width:172px;height:36px">Explore our services</a>
</section>

<section>
  <h2 class="abs display section-title" style="top:1464px;font-size:30px;color:#222">Our services</h2>
  <p class="abs section-title" style="top:1508px;font-size:12px;color:var(--muted)">Comprehensive support for every stage of your technical and energy projects.</p>
  <article class="card" style="left:109px"><div class="img" style="background:linear-gradient(135deg,#8a8f94,#c9ccd0)" role="img" aria-label="Technician checking energy readings on a tablet"></div><h4>Energy monitoring<br>&amp; optimization</h4><p>Monitor, analyze, and improve your energy performance...</p></article>
  <article class="card" style="left:358px"><div class="img" style="background:linear-gradient(135deg,#2f3a44,#6b7480)" role="img" aria-label="Project manager planning at a desk"></div><h4>Project planning<br>&amp; management</h4><p>From design to completion, our experts ensure every project...</p></article>
  <article class="card" style="left:607px"><div class="img" style="background:linear-gradient(135deg,#c9ccd0,#7d848c)" role="img" aria-label="Consultants reviewing technical drawings"></div><h4>Technical<br>consulting</h4><p>In-depth consulting for cooling, ventilation, heating, and...</p></article>
  <article class="card" style="left:856px"><div class="img" style="background:linear-gradient(135deg,#1f4f5a,#3c7a86)" role="img" aria-label="Team meeting in front of a data analysis screen"></div><h4>Operational<br>analysis...</h4><p>Detailed inspections and performance analyses...</p></article>
  <a class="btn" style="left:514px;top:1855px;width:172px;height:34px">View all services</a>
</section>

<section class="opt">
  <div class="photo" style="left:113px;top:2061px;width:209px;height:282px;background:linear-gradient(135deg,#8b8680,#d8d3cc)" role="img" aria-label="Consultant presenting a small wind turbine model"></div>
  <div class="photo" style="left:878px;top:2004px;width:208px;height:281px;background:linear-gradient(135deg,#4a5a6a,#9aa6b2 60%,#e0a33a)" role="img" aria-label="Tablet showing a solar panel monitoring app"></div>
  <h2 class="abs display">Continuous energy<br>optimization simplified</h2>
  <p class="abs">Our subscription-based energy monitoring platform provides real-time insights, regular reports, and optimization recommendations — helping you reduce costs and environmental impact without extra effort.</p>
  <a class="btn" style="left:514px;top:2234px;width:172px;height:34px">Subscribe now</a>
</section>

<section>
  <div class="abs sectors"></div>
  <h2 class="abs display" style="left:114px;top:2588px;color:#fff;font-size:25px;width:470px">Trusted by leading<br>commercial sectors</h2>
  <p class="abs" style="left:114px;top:2670px;color:#fff;font-size:12px">We deliver energy-efficient and technically sound solutions across industries:</p>
  <a class="btn" style="left:114px;top:2703px;width:172px;height:36px">Request a quote</a>
  <span class="arrow" style="left:495px;background:var(--orange)"><svg width="8" height="10"><path d="M6 1 L2 5 L6 9" stroke="#fff" fill="none" stroke-width="1.5"/></svg></span>
  <span class="arrow" style="left:541px;background:#fff"><svg width="8" height="10"><path d="M2 1 L6 5 L2 9" stroke="#333" fill="none" stroke-width="1.5"/></svg></span>
  <article class="sector" style="left:608px;width:236px"><div class="img" style="background:linear-gradient(135deg,#c8b79e,#8a7560)" role="img" aria-label="Property owner reviewing plans in a building"></div><h4>Commercial<br>property owners</h4></article>
  <article class="sector" style="left:856px;width:233px"><div class="img" style="background:linear-gradient(135deg,#d9d2c4,#8d8576)" role="img" aria-label="Grocery store aisles"></div><h4>Grocery retail<br>&amp; supermarkets</h4></article>
  <article class="sector" style="left:1104px;width:96px;overflow:hidden"><div class="img" style="background:linear-gradient(135deg,#7f8fa0,#b3bcc6)" role="img" aria-label="Construction site"></div><h4 style="text-align:left;padding-left:56px;white-space:nowrap">Construction<br>companies</h4></article>
</section>

<section class="contact">
  <div class="photo" style="left:188px;top:2998px;width:403px;height:544px;background:linear-gradient(135deg,#c6cfd6,#7f8a93 50%,#c9dc4a)" role="img" aria-label="Engineer in a hard hat and safety vest on a phone call"></div>
  <h2 class="abs display">Let's make your<br>energy systems<br>smarter</h2>
  <div class="field">
    <label style="left:673px;top:3185px">Name*</label><div class="input" style="top:3199px">Enter your name</div>
    <label style="left:673px;top:3242px">Company*</label><div class="input" style="top:3256px">Enter company name</div>
    <label style="left:673px;top:3299px">Email*</label><div class="input" style="top:3313px">Enter email</div>
    <label style="left:673px;top:3356px">Message*</label><div class="input" style="top:3370px;height:77px"></div>
  </div>
  <a class="btn" style="left:674px;top:3472px;width:172px;height:34px">Request a quote</a>
</section>

<footer>
  <div class="abs footer"></div>
  <div class="abs banner" role="img" aria-label="Partner banner with a smiling engineer in the background"></div>
  <div class="abs" style="left:147px;top:3652px;width:122px;height:122px;background:#fff"></div>
  <h2 class="abs display" style="left:300px;width:600px;text-align:center;top:3688px;color:#fff;font-size:24px">Norvik energy solutions</h2>
  <p class="abs" style="left:300px;width:600px;text-align:center;top:3728px;color:#fff;font-size:11px">Reliable partner for energy monitoring and technical consulting.</p>
  <span class="abs" style="left:947px;top:3686px;width:62px;height:54px;background:#fff;display:flex;align-items:center;justify-content:center"><svg width="18" height="12"><path d="M1 6 H16 M11 1 L16 6 L11 11" stroke="#333" fill="none" stroke-width="1.4"/></svg></span>

  <div class="abs logo" style="left:149px;top:3940px;color:#fff">VALOMIR</div>
  <div class="abs" style="left:171px;top:3991px;display:flex;gap:15px">
    <span style="width:41px;height:41px;background:rgba(255,255,255,.15)"></span>
    <span style="width:41px;height:41px;background:rgba(255,255,255,.15)"></span>
    <span style="width:41px;height:41px;background:rgba(255,255,255,.15)"></span>
  </div>
  <h3 class="abs foot-h" style="left:410px">Quick link</h3>
  <ul class="abs foot-list" style="left:410px"><li>About Us</li><li>Our Services</li><li>Projects</li><li>Blog</li><li>Contact Us</li></ul>
  <h3 class="abs foot-h" style="left:560px">Information</h3>
  <ul class="abs foot-list" style="left:560px"><li>Have feedback?</li><li>Let us know!</li><li>Privacy Policy</li><li>Terms of Use</li><li>Locations</li></ul>
  <h3 class="abs foot-h" style="left:723px">Subscribe newsletter</h3>
  <p class="abs" style="left:725px;top:3938px;color:#fff;font-size:10px;line-height:1.6;width:260px">Get our monthly newsletter and marketing tips, straight to your inbox</p>
  <div class="abs" style="left:723px;top:3989px;width:275px;height:40px;background:#fff;border:2px solid var(--orange);font-size:10px;color:#888;padding:11px 14px">Enter your email</div>
  <a class="btn" style="left:884px;top:3991px;width:112px;height:36px">Subscribe</a>
  <div class="abs" style="left:149px;top:4148px;width:900px;border-top:1px solid rgba(255,255,255,.3)"></div>
  <p class="abs section-title" style="top:4164px;color:#fff;font-size:10px">© 2025 global valomir. All rights reserved.</p>
  <span class="abs" style="left:1024px;top:4127px;width:49px;height:42px;background:var(--orange);display:flex;align-items:center;justify-content:center"><svg width="20" height="16"><path d="M3 2 H17 V11 H8 L4 14 V11 H3 Z" fill="#fff"/></svg></span>
</footer>

</body>
</html>
```